Psychotherapy Practice Needs Non-Corporate Stationary

I need an elegant design for letterhead, envelope, and note card for my psychotherapy private practice in Silicon Valley. I work with pre-teens, teens, and adults primarily with anxiety, stress, and depression.

Stationary should convey warmth and professionalism. I tend to like somewhat modern designs.

My business card is already done--attached here for reference.

Target Market(s)

Professionals of Silicon Valley, Academic Advisors at High Schools, Psychologists, Psychiatrists, Pediatricians, Directors of Human Resources, Community leaders

Industry/Entity Type

Psychology

Font styles to use
Serif

Requirements
Must have
• Logo attached--can use with or without the name included. Feel free to move the name to the right of the logo. I included all versions just in case. Colors to use should match or go with the logo (greens, maybe blues if they go), but can be somewhat softer than the bold greens and browns used. (Ex. more sage green vs. kelly green)
• Letterhead--please include the following:
• Marisol Quenneville, LMFT
• 318 Bellweather Lane, Suite 15
• Palo Alto, CA 94317
• 650-555-0187
• marisol@marisolquenneville.example
• marisolquenneville.example
• Envelope--please include:
• Marisol Quenneville, LMFT
• Palo Alto, CA 94317
• 650-555-0187
• marisolquenneville.example
• Note Card--please include:
• Marisol Quenneville, LMFT
• 650-555-0187
• marisolquenneville.example
Nice to have
• I'd love to see examples both with and without a logo watermark in the background. I especially like the watermark towards the lower right corner for the letterhead. I'd also like to see some versions of the letterhead with all contact info at the bottom.
Should not have
• It should not be corporate and should avoid harsh lines.

```html
<!DOCTYPE html>
<html lang="en">
<head>
<meta charset="utf-8">
<title>Marisol Quenneville, LMFT — Stationery</title>
<link rel="stylesheet" href="https://fonts.googleapis.com/css2?family=Marcellus+SC&family=Lato:wght@400&family=Crimson+Text&family=Great+Vibes&display=swap">
<style>
:root{
  --board:#d6d6d6;
  --paper:#f1f1f1;
  --paper-edge:#e2e2e2;
  --ink:#2b2622;
  --ink-soft:#4a4440;
  --leaf:#2f8a3f;
  --leaf-light:#7cbd4a;
  --sage-wash:#dfe6e0;
  --sage-faint:#e6ebe6;
  --script:#6aa83a;
  --rule:#d5d5d5;
  --coil:#8a8a8a;
}
*{box-sizing:border-box;margin:0;padding:0}
html,body{width:1039px;height:1200px;overflow:hidden}
body{background:var(--board);position:relative;font-family:"Lato",sans-serif;color:var(--ink)}
.piece{position:absolute;background:var(--paper);overflow:hidden;box-shadow:0 1px 3px rgba(0,0,0,.18)}
.name{font-family:"Marcellus SC",serif;color:var(--ink);white-space:nowrap}
.mark-dot{display:block;border-radius:50%;background:radial-gradient(circle at 40% 40%,var(--leaf-light),var(--leaf))}
.watermark{position:absolute;border-radius:50%;background:radial-gradient(circle,var(--sage-wash) 0%,var(--sage-faint) 60%,rgba(230,235,230,0) 72%)}
.fine{font-family:"Crimson Text",serif;color:var(--ink-soft);white-space:nowrap}

/* letterhead cover */
.letterhead-cover{left:143px;top:79px;width:363px;height:467px}
.letterhead-cover .mark-dot{position:absolute;left:155px;top:34px;width:54px;height:54px}
.letterhead-cover .name{position:absolute;top:110px;width:100%;text-align:center;font-size:15px}
.letterhead-cover .watermark{left:30px;top:150px;width:300px;height:300px}
.letterhead-cover .site{position:absolute;bottom:32px;width:100%;text-align:center;font-family:"Crimson Text",serif;font-size:9.5px}

/* letter */
.letter{left:530px;top:79px;width:353px;height:467px}
.letter .mark-dot{position:absolute;left:60px;top:22px;width:30px;height:30px}
.letter .name{position:absolute;left:33px;top:60px;font-size:7.5px}
.letter .contact{position:absolute;left:228px;top:27px;border-left:1.5px solid var(--ink);padding-left:9px;font-size:5.3px;line-height:6.8px;height:47px}
.letter .watermark{left:80px;top:240px;width:260px;height:260px}
.letter .body{position:absolute;left:33px;top:110px;width:292px;font-size:5.9px;line-height:10.4px;color:var(--ink)}
.letter .body p{margin-bottom:10px;text-align:justify}
.letter .greet{margin-bottom:10px}
.letter .signature{position:absolute;left:33px;top:334px;width:105px;height:24px;background:linear-gradient(90deg,rgba(43,38,34,.25),rgba(43,38,34,.08))}
.letter .role{position:absolute;left:33px;top:369px;font-size:6.4px}

/* envelope front */
.envelope-front{left:114px;top:568px;width:392px;height:172px}
.envelope-front .mark-dot{position:absolute;left:40px;top:10px;width:33px;height:33px}
.envelope-front .name{position:absolute;left:16px;top:52px;font-size:7px}
.envelope-front .watermark{left:240px;top:-10px;width:180px;height:180px}
.envelope-front .contact{position:absolute;left:16px;top:146px;font-size:5.3px;line-height:11px}
.envelope-front .contact .line1{border-bottom:1px solid var(--ink);width:131px}

/* envelope back */
.envelope-back{left:530px;top:571px;width:395px;height:170px}
.envelope-back .flap{position:absolute;left:0;top:0}
.envelope-back .mark-dot{position:absolute;left:178px;top:10px;width:34px;height:34px;opacity:.3}

/* notebook */
.notebook{left:65px;top:776px;width:249px;height:353px;border-left:1px solid #9aa3b5}
.notebook .watermark{left:-20px;top:0;width:300px;height:330px}
.notebook .mark-dot{position:absolute;left:93px;top:127px;width:62px;height:62px}
.notebook .name{position:absolute;top:207px;width:100%;text-align:center;font-size:11px}
.coils{position:absolute;width:10px}
.coils span{display:block;height:2.5px;border-radius:2px;background:var(--coil);margin-bottom:18.7px}

/* notepad */
.notepad{left:355px;top:777px;width:250px;height:352px}
.notepad .mark-dot{position:absolute;left:108px;top:6px;width:34px;height:34px}
.notepad .name{position:absolute;top:50px;width:100%;text-align:center;font-size:7px}
.notepad .lines{position:absolute;left:0;right:0;top:69px;height:250px;background:repeating-linear-gradient(to bottom,transparent 0 15.5px,var(--rule) 15.5px 16.5px)}
.notepad .foot{position:absolute;bottom:8px;width:100%;text-align:center;font-size:4.6px}

/* compliment card */
.compliment-card{left:617px;top:754px;width:388px;height:199px}
.compliment-card .mark-dot{position:absolute;left:50px;top:14px;width:44px;height:44px}
.compliment-card .name{position:absolute;left:20px;top:68px;font-size:7.8px}
.compliment-card .watermark{left:210px;top:0;width:200px;height:200px}
.compliment-card .script{position:absolute;left:19px;top:147px;font-family:"Great Vibes",cursive;color:var(--script);font-size:17px}
.compliment-card .contact{position:absolute;left:20px;top:168px;font-size:5.6px;line-height:11px}
.compliment-card .contact .line1{border-bottom:1px solid var(--ink);width:186px}

/* large mark */
.hero-mark{position:absolute;left:723px;top:1000px;width:180px;height:180px;border-radius:50%;background:radial-gradient(circle at 40% 40%,var(--leaf-light),var(--leaf))}
</style>
</head>
<body>

<section class="piece letterhead-cover">
  <div class="watermark"></div>
  <span class="mark-dot"></span>
  <div class="name">Marisol Quenneville, LMFT</div>
  <div class="site">marisolquenneville.example</div>
</section>

<section class="piece letter">
  <div class="watermark"></div>
  <span class="mark-dot"></span>
  <div class="name">Marisol Quenneville, LMFT</div>
  <div class="contact fine">
    318 Bellweather Lane, Suite 15<br>Palo Alto, CA 94317<br>
    650-555-0187<br>marisol@marisolquenneville.example<br>marisolquenneville.example
  </div>
  <div class="body">
    <div class="greet">Dear Client</div>
    <p>Lorem ipsum dolor sit amet, consectetur adipiscing elit. Pellentesque semper purus ornare dolor eleifend aliquam. Integer molestie gravida sem a porttitor. Quisque pulvinar tellus ut ipsum molestie ultricies id non turpis. Phasellus feugiat ornare feugiat. Integer nec velit eu justo laoreet condimentum. Aenean non commodo quam, nec ultrices augue.</p>
    <p>Curabitur nec venenatis risus. Integer nec nisi sit amet leo mattis aliquam. Vivamus vulputate tellus quis purus lobortis rutrum. Aenean nec ipsum ut mauris faucibus facilisis vel porttitor neque. Morbi molestie magna id neque scelerisque ut iaculis justo porttitor. Sed est ligula, semper at cursus ac, porttitor ac ipsum.</p>
    <p>Maecenas vel neque ante, id faucibus ipsum. Suspendisse non neque quis nunc rhoncus bibendum. Fusce sit amet quam quis libero facilisis ultrices. Donec dignissim lorem vel sem sodales mollis. Duis nec sem lorem, at tristique nibh. Sed fringilla nisi non nunc facilisis in ullamcorper justo suscipit.</p>
  </div>
  <div class="signature" role="img" aria-label="Handwritten signature"></div>
  <div class="role">Managing Director</div>
</section>

<section class="piece envelope-front">
  <div class="watermark"></div>
  <span class="mark-dot"></span>
  <div class="name">Marisol Quenneville, LMFT</div>
  <div class="contact fine">
    <div class="line1">650-555-0187 | marisolquenneville.example</div>
    <div>318 Bellweather Lane | Suite 15 | Palo Alto | CA 94317</div>
  </div>
</section>

<section class="piece envelope-back">
  <svg class="flap" width="395" height="70" viewBox="0 0 395 70" aria-hidden="true">
    <path d="M1 0 L10 48 Q14 60 28 60 L367 60 Q381 60 385 48 L394 0" fill="none" stroke="#bdbdbd" stroke-width="1"/>
  </svg>
  <span class="mark-dot"></span>
</section>

<div class="coils" style="left:58px;top:788px"><span></span><span></span><span></span><span></span><span></span><span></span><span></span><span></span><span></span><span></span><span></span><span></span><span></span><span></span><span></span><span></span><span></span></div>
<section class="piece notebook">
  <div class="watermark"></div>
  <span class="mark-dot"></span>
  <div class="name">Marisol Quenneville, LMFT</div>
</section>

<section class="piece notepad">
  <span class="mark-dot"></span>
  <div class="name">Marisol Quenneville, LMFT</div>
  <div class="lines"></div>
  <div class="foot fine">650-555-0187 | marisol@marisolquenneville.example | marisolquenneville.example</div>
</section>
<div class="coils" style="left:350px;top:790px;width:18px"><span></span><span></span><span></span><span></span><span></span><span></span><span></span><span></span><span></span><span></span><span></span><span></span><span></span><span></span><span></span><span></span><span></span></div>

<section class="piece compliment-card">
  <div class="watermark"></div>
  <span class="mark-dot"></span>
  <div class="name">Marisol Quenneville, LMFT</div>
  <div class="script">With Compliments</div>
  <div class="contact fine">
    <div class="line1">650-555-0187 | marisol@marisolquenneville.example | marisolquenneville.example</div>
    <div>318 Bellweather Lane | Suite 15 | Palo Alto | CA 94317</div>
  </div>
</section>

<div class="hero-mark"></div>

</body>
</html>
```